Doorhanger logo and design

Company is called "Beamwell TV" would like a logo created for it, with colors if red, white and blue. Example would be a tv with a remote or antenna ect...doorhanger size is 3.5x8.5 in which I am using quorvaprint.example so it needs to fit within the size thanks.

Industry/Entity Type

Tv

```html
<!DOCTYPE html>
<html lang="en">
<head>
<meta charset="utf-8">
<title>Beamwell TV Door Hanger</title>
<link rel="stylesheet" href="https://fonts.googleapis.com/css2?family=Oswald:wght@500;600&family=Signika:wght@600&family=Ubuntu:wght@400;700&display=swap">
<style>
  :root {
    --brand-red: #e3232c;
    --deep-red: #b3161f;
    --navy: #1d2170;
    --navy-dark: #151552;
    --royal: #2a3595;
    --paper: #f7f7f7;
    --paper-shade: #e4e4e4;
    --hole: #555555;
    --ring: #c4c4c4;
    --stage: #ececec;
  }
  html, body { margin: 0; padding: 0; overflow: hidden; }
  body {
    width: 1200px; height: 1200px;
    background: var(--stage);
    display: flex; justify-content: center; align-items: center; gap: 68px;
  }
  .hanger { width: 433px; height: 1050px; display: block; box-shadow: 0 6px 18px rgba(0,0,0,.25); }
  .brand-name { font-family: "Signika", "Trebuchet MS", sans-serif; font-weight: 600; font-size: 50px; fill: var(--brand-red); }
  .headline { font-family: "Oswald", "Arial Narrow", sans-serif; font-weight: 600; fill: #fff; }
  .call-label { font-family: "Ubuntu", Arial, sans-serif; font-size: 29px; fill: #fff; }
  .call-number { font-family: "Ubuntu", Arial, sans-serif; font-weight: 700; font-size: 42px; fill: #fff; }
</style>
</head>
<body>

<svg class="hanger hanger-front" viewBox="0 0 541 1312" aria-label="Door hanger front">
  <defs>
    <linearGradient id="paperFront" x1="0" y1="0" x2="1" y2="1">
      <stop offset="0" stop-color="var(--paper-shade)"/><stop offset=".5" stop-color="var(--paper)"/><stop offset="1" stop-color="var(--paper-shade)"/>
    </linearGradient>
    <linearGradient id="navyFront" x1="0" y1="0" x2="0" y2="1">
      <stop offset="0" stop-color="var(--royal)"/><stop offset="1" stop-color="var(--navy-dark)"/>
    </linearGradient>
    <linearGradient id="photoSport" x1="0" y1="0" x2="1" y2="1">
      <stop offset="0" stop-color="#7b6f86"/><stop offset=".5" stop-color="#6d7c5a"/><stop offset="1" stop-color="#3a3a3c"/>
    </linearGradient>
    <clipPath id="clipFront"><rect width="541" height="1312"/></clipPath>
  </defs>
  <g clip-path="url(#clipFront)">
    <rect class="paper" width="541" height="1312" fill="url(#paperFront)"/>
    <path class="corner-band" d="M0 0 H175 C110 60 40 150 0 265 Z" fill="var(--brand-red)"/>
    <g class="corner-lines" fill="none" stroke="#e8836b" stroke-width="1.5">
      <path d="M0 275 C90 90 300 10 541 20"/>
      <path d="M0 285 C100 95 310 18 541 30"/>
      <path d="M0 295 C110 100 320 26 541 40"/>
      <path d="M0 305 C120 110 330 34 541 50"/>
    </g>
    <circle class="hang-hole" cx="270" cy="157" r="110" fill="var(--hole)" stroke="var(--ring)" stroke-width="8"/>
    <text class="brand-name" x="270" y="382" text-anchor="middle">Beamwell TV</text>

    <g class="wave-lines" fill="none" stroke="#e2a591" stroke-width="1.2">
      <path d="M0 790 C120 800 200 860 260 940"/>
      <path d="M0 810 C120 820 200 880 250 960"/>
      <path d="M0 830 C110 840 190 900 240 980"/>
    </g>
    <path class="bottom-field" d="M0 900 C200 960 400 950 541 880 V1312 H0 Z" fill="url(#navyFront)"/>
    <g class="blue-wave-lines" fill="none" stroke="#3f70c0" stroke-width="2">
      <path d="M0 915 C150 900 300 920 400 960"/>
      <path d="M0 945 C150 930 300 950 400 990"/>
      <path d="M0 975 C150 960 300 980 400 1020"/>
    </g>

    <circle class="photo-ring" cx="313" cy="702" r="265" fill="var(--ring)"/>
    <circle class="photo" cx="313" cy="702" r="243" fill="url(#photoSport)" role="img" aria-label="Photo of a hand holding a remote in front of a TV showing football"/>
    <circle class="accent-disc" cx="100" cy="590" r="133" fill="var(--deep-red)" opacity=".93"/>
    <text class="headline" x="93" y="594" font-size="42" text-anchor="middle">TEXT HERE</text>

    <text class="headline" x="270" y="1165" font-size="104" text-anchor="middle">TEXT HERE</text>
    <rect class="call-bar" y="1249" width="541" height="52" fill="var(--brand-red)"/>
    <text x="33" y="1287"><tspan class="call-label">Call Us Now </tspan><tspan class="call-number" dx="4">123 456 7890</tspan></text>
  </g>
</svg>

<svg class="hanger hanger-back" viewBox="0 0 541 1312" aria-label="Door hanger back">
  <defs>
    <linearGradient id="paperBack" x1="0" y1="0" x2="1" y2="1">
      <stop offset="0" stop-color="var(--paper-shade)"/><stop offset=".5" stop-color="#fff"/><stop offset="1" stop-color="var(--paper-shade)"/>
    </linearGradient>
    <linearGradient id="navyBack" x1="0" y1="0" x2="0" y2="1">
      <stop offset="0" stop-color="var(--royal)"/><stop offset="1" stop-color="var(--navy)"/>
    </linearGradient>
    <linearGradient id="photoRoom" x1="0" y1="0" x2="1" y2="1">
      <stop offset="0" stop-color="#d9d3c8"/><stop offset=".5" stop-color="#a8b98a"/><stop offset="1" stop-color="#eeeeee"/>
    </linearGradient>
    <clipPath id="clipBack"><rect width="541" height="1312"/></clipPath>
  </defs>
  <g clip-path="url(#clipBack)">
    <rect class="paper" width="541" height="1312" fill="url(#paperBack)"/>
    <path class="side-swoosh" d="M0 0 H38 C60 420 260 800 541 960 V1312 H0 Z" fill="url(#navyBack)"/>
    <g class="swoosh-lines" fill="none" stroke="#fff" stroke-width="2">
      <path d="M8 0 C30 420 240 820 541 990"/>
      <path d="M18 0 C40 420 250 815 541 1010"/>
      <path d="M28 0 C50 420 260 810 541 1035"/>
      <path d="M38 0 C60 420 270 805 541 1055"/>
    </g>
    <circle class="hang-hole" cx="270" cy="157" r="110" fill="var(--hole)" stroke="var(--ring)" stroke-width="8"/>
    <text class="brand-name" x="270" y="382" text-anchor="middle">Beamwell TV</text>
    <circle class="accent-disc" cx="425" cy="740" r="152" fill="var(--deep-red)" opacity=".95"/>
    <circle class="photo-ring" cx="200" cy="1072" r="275" fill="var(--ring)"/>
    <circle class="photo" cx="200" cy="1072" r="253" fill="url(#photoRoom)" role="img" aria-label="Photo of a living room with a wall-mounted TV and a viewer on the rug"/>
  </g>
</svg>

</body>
</html>
```